Australian Export Wine Label

Brand

To design a label based around Australia’s famous bush ranger Sam Ordway called Ordway’s Run.

Imagery for the label could be an abstract image of Sam’s armour of even of himself or we are open to other possibilities ranging from a traditional label to a more contemporary look and feel.

Images should not include guns and imagery used must be free of copyright.

Designs should be able to be printed by the standard 4 colour print process. As this is not an expensive product there will be no expensive label fiunishes such as gold foil or embossing

The range

The range of wines will consist of a 2011 Shiraz, 2012 Sauvignon Blanc and 2011 Chardonnay.

Market

The primary market for these wines is Ireland with the price range being in the $10-15 bracket. The wines will be available in independent retail shops and restaurants

Front Label Mandatories

1. Front Label: should not exceed 110mm x 80mm

2. Brand name - Ordway’s Run

3. Vintage & Variety – for example 2011 Shiraz

4. Origin – Wine of Australia

5. Text to appear on front label: Born in Co. Antrim, the remarkable Ruth Ordway had eight children including Australia’s most famous Bushranger Sam Ordway. The family’s wild and independent spirit is legendary in country Australia.

Back Label Mandatories

1. Back Label: 80mm x 80mm

2. Brand name

3. Vintage & Variety

4. Alcohol, Volume, Country of production

5. 13.0% VOL 750Ml (must be 4mm in height)

6. Contains egg, milk and nuts. Traces may remain

7. Please include the pregnant lady logo and a recycling logo

8. Wine of Australia

9. Space for barcode

10. Text to appear on back label (Shiraz):

Ordway’s Run is our vineyard named after the Ordway family, whose homestead stood here long before the vines were planted.
Our Ordway’s Run Shiraz is bold and full of flavour. Plums, cassis, chocolate and spice intermingle on the nose and palate, resulting in a full bodied, vibrant wine. Enjoy with a spirit of adventure and a hearty beef stew.

```html
<!DOCTYPE html>
<html lang="en">
<head>
<meta charset="utf-8">
<title>Ordway’s Run — Shiraz Labels</title>
<link rel="stylesheet" href="https://fonts.googleapis.com/css2?family=Cinzel:wght@400;500&family=Cormorant+Garamond:ital,wght@0,400;0,500;1,400&display=swap">
<style>
  :root {
    --paper: #ffffff;
    --label: #fbfbf9;
    --wine: #7a1f3a;
    --ink: #2a2a2a;
    --muted: #6d6d6d;
    --rule: #8a8a8a;
    --art: #c9c6c0;
  }
  * { box-sizing: border-box; margin: 0; padding: 0; }
  html, body { width: 1200px; height: 837px; overflow: hidden; background: var(--paper); }
  .canvas {
    width: 1200px; height: 837px;
    display: flex; align-items: center; justify-content: center; gap: 80px;
    font-family: "Cormorant Garamond", Georgia, serif;
    color: var(--ink);
  }

  /* Front label */
  .front-label {
    width: 320px; height: 600px;
    background: var(--label);
    border: 1px solid #e2e0db;
    box-shadow: 0 2px 10px rgba(0,0,0,.08);
    display: flex; flex-direction: column; align-items: center;
    padding: 46px 34px 40px;
    text-align: center;
  }
  .front-label .armour-art {
    width: 64px; height: 120px;
    background: linear-gradient(180deg, #d8d5cf, var(--art) 60%, #a9a59e);
    border-radius: 6px;
  }
  .front-label .brand {
    margin-top: 40px;
    font-family: "Cinzel", "Times New Roman", serif;
    font-weight: 400;
    color: var(--wine);
    font-size: 58px; line-height: 1.02; letter-spacing: 2px;
  }
  .front-label .variety {
    margin-top: 36px;
    font-family: "Cinzel", serif; font-size: 15px; letter-spacing: 3px; color: var(--wine);
  }
  .front-label .origin, .front-label .vintage {
    font-family: "Cinzel", serif; font-size: 12px; letter-spacing: 3px; color: var(--muted);
    margin-top: 6px;
  }
  .front-label .story {
    margin-top: 40px;
    font-size: 14px; line-height: 1.55; color: var(--muted);
  }

  /* Back label */
  .back-label {
    width: 320px; height: 420px;
    background: var(--label);
    border: 1px solid #e2e0db;
    box-shadow: 0 2px 10px rgba(0,0,0,.08);
    padding: 14px;
  }
  .back-label .frame {
    border: 1px solid var(--rule);
    height: 100%;
    display: flex; flex-direction: column;
  }
  .back-label .brand {
    font-family: "Cinzel", serif; color: var(--wine);
    font-size: 30px; text-align: center; letter-spacing: 1px;
    padding: 12px 0 10px;
    border-bottom: 1px solid var(--rule);
  }
  .back-label .variety-line {
    font-family: "Cinzel", serif; font-size: 11px; letter-spacing: 2.5px;
    color: var(--muted); text-align: center;
    padding: 12px 0;
    border-bottom: 1px solid var(--rule);
  }
  .back-label .body {
    flex: 1; display: flex; gap: 10px; padding: 14px 12px;
    border-bottom: 1px solid var(--rule);
  }
  .back-label .copy { font-size: 14px; line-height: 1.35; }
  .back-label .copy em { font-style: italic; }
  .back-label .symbols { width: 30px; flex: none; }
  .back-label .recycle-icon { width: 26px; height: 26px; }
  .back-label .legal { padding: 10px 12px; }
  .back-label .abv { font-size: 13px; letter-spacing: .5px; }
  .back-label .allergens { font-size: 10px; color: var(--muted); margin-top: 2px; }
</style>
</head>
<body>
<main class="canvas">
  <section class="front-label" aria-label="Front label">
    <div class="armour-art" role="img" aria-label="Engraved illustration of a bushranger’s iron armour"></div>
    <h1 class="brand">Ordway’s<br>Run</h1>
    <p class="variety">SHIRAZ</p>
    <p class="origin">WINE OF AUSTRALIA</p>
    <p class="vintage">2011</p>
    <p class="story">Born in Co. Antrim, the remarkable <em>Ruth Ordway</em> had eight children including Australia’s most famous Bushranger <em>Sam Ordway</em>. The family’s wild and independent spirit is legendary in country Australia.</p>
  </section>

  <section class="back-label" aria-label="Back label">
    <div class="frame">
      <h2 class="brand">ORDWAY’S RUN</h2>
      <p class="variety-line">SHIRAZ &nbsp;|&nbsp; WINE OF AUSTRALIA</p>
      <div class="body">
        <p class="copy"><em>Ordway’s Run</em> is our vineyard named after the Ordway family, whose homestead stood here long before the vines were planted. Our <em>Ordway’s Run Shiraz</em> is bold and full of flavour. Plums, cassis, chocolate and spice intermingle on the nose and palate, resulting in a full bodied, vibrant wine. Enjoy with a spirit of adventure and a hearty beef stew.</p>
        <div class="symbols">
          <svg class="recycle-icon" viewBox="0 0 26 26" aria-label="Recycling symbol" role="img">
            <circle cx="13" cy="13" r="12" fill="none" stroke="#2a2a2a" stroke-width="1.5"/>
            <path d="M7 15 A6 6 0 0 1 17 8" fill="none" stroke="#2a2a2a" stroke-width="2"/>
            <path d="M19 11 A6 6 0 0 1 9 18" fill="none" stroke="#2a2a2a" stroke-width="2"/>
            <path d="M15 6 L18 8 L15 10 Z" fill="#2a2a2a"/>
            <path d="M11 16 L8 18 L11 20 Z" fill="#2a2a2a"/>
          </svg>
        </div>
      </div>
      <div class="legal">
        <p class="abv">13.0% VOL 750Ml</p>
        <p class="allergens">Contains egg, milk and nuts. Traces may remain</p>
      </div>
    </div>
  </section>
</main>
</body>
</html>
```